*** Business Card Design Project

I need a logo and business card for my new catering business: "Pomelia". The design should be modern, clean, elegant and refined. One or Two colours only. The design SHOULD NOT include graphics or images. There should be space for my name, phone number and email address (I will provide these to you later).

Industry/Entity Type

Catering

Requirements
Must have
• Must have one or two colours only.
Must include the text "pomelia"
Should not have
• Must not have graphics or images.

```html
<!DOCTYPE html>
<html lang="en">
<head>
<meta charset="utf-8">
<title>Pomelia – Business Cards</title>
<link rel="stylesheet" href="https://fonts.googleapis.com/css2?family=Arvo:wght@400;700&family=Didact+Gothic&display=swap">
<style>
  :root {
    --backdrop: #e7e4df;
    --card-stock: #eeefea;
    --brand-green: #7cc243;
    --card-shadow: rgba(40, 30, 20, 0.22);
  }
  html, body {
    margin: 0;
    padding: 0;
    overflow: hidden;
  }
  .canvas {
    position: relative;
    width: 1200px;
    height: 880px;
    background: var(--backdrop);
    overflow: hidden;
  }
  .card {
    position: absolute;
    width: 580px;
    height: 332px;
    background: var(--card-stock);
    box-shadow: 0 6px 18px var(--card-shadow);
    box-sizing: border-box;
  }
  .card-front {
    left: 540px;
    top: 110px;
    display: flex;
    align-items: center;
    justify-content: center;
  }
  .wordmark {
    font-family: "Arvo", Georgia, serif;
    font-weight: 700;
    font-size: 84px;
    letter-spacing: 3px;
    color: var(--brand-green);
    margin: 0;
    line-height: 1;
  }
  .card-back {
    left: 80px;
    top: 440px;
    display: flex;
    flex-direction: column;
    align-items: center;
    justify-content: center;
  }
  .holder-name {
    font-family: "Arvo", Georgia, serif;
    font-weight: 700;
    font-size: 34px;
    letter-spacing: 1.5px;
    color: var(--brand-green);
    margin: 0 0 10px;
    line-height: 1.1;
  }
  .name-rule {
    display: block;
    width: 430px;
    height: 4px;
    margin: 0 0 12px;
  }
  .contact-line {
    font-family: "Didact Gothic", "Helvetica Neue", Arial, sans-serif;
    font-size: 20px;
    letter-spacing: 0.5px;
    color: var(--brand-green);
    margin: 0;
    white-space: nowrap;
  }
  .contact-separator {
    display: inline-block;
    width: 6px;
    height: 6px;
    border-radius: 50%;
    background: var(--brand-green);
    margin: 0 12px;
    vertical-align: middle;
  }
</style>
</head>
<body>
<main class="canvas">
  <section class="card card-front" aria-label="Card front">
    <h1 class="wordmark">POMELIA</h1>
  </section>

  <section class="card card-back" aria-label="Card back">
    <h2 class="holder-name">ADRIAN MOORE</h2>
    <svg class="name-rule" viewBox="0 0 430 4" aria-hidden="true">
      <polygon points="0,2 215,0.5 430,2 215,3.5" fill="var(--brand-green)"/>
    </svg>
    <p class="contact-line">
      <span class="contact-phone">(+00) 482 915 630</span><span class="contact-separator" aria-hidden="true"></span><span class="contact-email">ADRIAN@POMELIA.COM</span>
    </p>
  </section>
</main>
</body>
</html>
```